Marlow Bay Kestrel Arrivals Flyer

A 2 sided DL size flyer. (Approx 20cm long by 10cm wide)
That has logo and blurb about company on front. On back details of Kestrel arrivals package, trademark, contact details and license numbers.
We feel we need to see the text on the flyer design and then make some changes so there will be some back and forth about written content. There may be a reduction in the amount of text we want for the blurb about the company but the rest is mandatory.
Our logo is blue and green, we do not want a white flyer with black text as feel this looks homemade so we need your suggestions about what colour the text and flyer could be.
We want the flyer to look clean and modern. It will go on a stand at an immigration fair and will be sent in the post and via email to clients. We will need posters at a later stage.
Migrants
It Company

```html
<!DOCTYPE html>
<html lang="en">
<head>
<meta charset="utf-8">
<title>Marlow Bay Kestrel Arrivals – DL Flyer</title>
<link href="https://fonts.googleapis.com/css2?family=Open+Sans:ital,wght@0,400;0,600;0,700;1,600;1,700&display=swap" rel="stylesheet">
<style>
:root{
  --blue:#1b5fae;
  --navy:#0b2d66;
  --navy-light:#1b4d9a;
  --green:#3aaa35;
  --green-dark:#2e8f2a;
  --badge:#a7b36b;
  --text:#3d3d3d;
  --muted:#6b6b6b;
  --bg:#e6e6e6;
  --shade:#e4e4ef;
}
*{box-sizing:border-box;margin:0;padding:0}
html,body{width:1200px;height:1178px;overflow:hidden}
body{background:var(--bg);font-family:"Open Sans",Arial,sans-serif;color:var(--text);position:relative}
.flyer{position:absolute;top:89px;width:470px;height:1000px;background:#fff;overflow:hidden;box-shadow:0 6px 18px rgba(0,0,0,.25)}
.flyer--front{left:120px}
.flyer--back{left:640px}
.photo{position:absolute;left:0;top:0;width:470px}
.photo--family{height:390px;background:linear-gradient(180deg,#8a9aa8 0%,#c9d3dc 30%,#a58c7a 60%,#6d5748 100%)}
.photo--students{height:310px;background:linear-gradient(160deg,#c7a98c 0%,#e6d6c3 40%,#6f86a6 70%,#d9c25a 100%)}
.swoosh{position:absolute;left:0;width:470px}
.badge{position:absolute;border-radius:50%;background:var(--badge);border:4px solid #d9d9d9;box-shadow:0 2px 5px rgba(0,0,0,.3)}
.logo{position:absolute;display:flex;align-items:center;gap:14px}
.logo__mark{border-radius:50%;border:7px solid var(--green);background:#fff}
.logo__name{color:var(--blue);font-weight:700;line-height:1.1;border-left:2px solid #333;padding-left:10px}
.center{position:absolute;left:0;width:470px;text-align:center}
.headline{color:var(--blue);font-size:16px;top:526px}
.pill{position:absolute;background:var(--green);color:#fff;border-radius:16px;text-align:center}
.body-copy{position:absolute;left:22px;width:430px;font-size:11px;line-height:15px;text-align:justify}
.quote{position:absolute;left:30px;top:762px;width:410px;height:60px;border:1px dotted var(--green);font-size:13px;line-height:22px;padding:6px 10px 0 40px}
.quote__mark{position:absolute;left:8px;top:-8px;color:var(--green);font-size:40px;font-weight:700}
.footer{position:absolute;left:0;bottom:0;width:470px;height:100px}
.footer__text{position:absolute;left:0;width:470px;top:32px;text-align:center;color:#fff;font-size:11px;line-height:17px}
.footer__web{font-size:16px;font-weight:700;letter-spacing:.3px}
.social{position:absolute;left:24px;top:44px;width:38px;height:38px;border-radius:50%;background:var(--green)}
.package-title{top:328px;font-size:16px;color:var(--blue)}
.benefits{position:absolute;left:20px;top:450px;width:430px;list-style:none;font-size:11px;line-height:15px}
.benefits li{position:relative;padding-left:17px;margin-bottom:10px}
.benefits li::before{content:"";position:absolute;left:0;top:3px;width:9px;height:9px;border-radius:50%;background:var(--green)}
.plan{position:absolute;left:20px;top:630px;width:436px;height:130px;border:1px dotted var(--green);display:flex}
.plan__col{flex:1;text-align:center;font-size:10px;line-height:13.5px;padding:32px 6px 0;color:var(--muted)}
.plan__col--shade{background:var(--shade)}
.plan__num{display:block;font-size:26px;color:var(--green);margin-bottom:8px;line-height:1}
.addons{top:768px;font-size:11px}
.tagline{top:790px;font-size:11px;color:var(--green-dark);font-style:italic;font-weight:700}
.contacts{position:absolute;left:252px;top:820px;font-size:11px;line-height:14px;color:var(--muted)}
.contacts dt{color:var(--blue);font-weight:600;display:flex;gap:10px}
.contacts dt span{color:var(--text);font-weight:400}
.contacts dd{margin-bottom:6px}
</style>
</head>
<body>

<section class="flyer flyer--front">
  <div class="photo photo--family" role="img" aria-label="Smiling family of four in front of a snow-capped mountain and lake"></div>
  <svg class="swoosh" style="top:300px" width="470" height="100" viewBox="0 0 470 100">
    <path d="M0 30 Q200 95 470 20 L470 100 L0 100Z" fill="var(--green)"/>
    <path d="M0 42 Q200 110 470 34 L470 100 L0 100Z" fill="#fff"/>
  </svg>
  <div class="badge" style="left:368px;top:306px;width:88px;height:88px" role="img" aria-label="Licensing authority badge"></div>

  <div class="logo" style="left:60px;top:412px">
    <div class="logo__mark" style="width:82px;height:82px"></div>
    <div class="logo__name" style="font-size:22px">Marlow Bay<br>Kestrel Arrivals<br><span style="font-size:14px;letter-spacing:2px">Immigration Advice</span></div>
  </div>

  <h1 class="center headline" style="font-weight:400">FRIENDLY &amp; HELPFUL LICENSED IMMIGRATION ADVISERS</h1>
  <div class="pill" style="left:41px;top:562px;width:388px;height:30px;line-height:30px;font-size:14px">WE FACILITATE FAST AND PROBLEM FREE VISAS</div>

  <p class="body-copy" style="top:616px">Marlow Bay Kestrel Arrivals is a family business; headed by two sisters – Maren and Isla Thorne. Originally from the UK they migrated to New Zealand over ten years ago, so understand how it feels to move to a new country &amp; go through the visa process.</p>
  <p class="body-copy" style="top:691px">Isla &amp; Maren are passionate about what New Zealand has to offer and enjoy the chance to help people make their home here. They work across all types of visa applications – <b><i>to live, work or study.</i></b></p>

  <blockquote class="quote"><span class="quote__mark">“</span>Working closely with you to meet your immigration goals, we help and guide you at every stage.”</blockquote>

  <p class="body-copy" style="top:848px">Trained and qualified, they have specialist knowledge of the immigration system. Able to work to urgent timeframes or with clients who have character or health issues.</p>

  <footer class="footer">
    <svg width="470" height="100" viewBox="0 0 470 100" style="position:absolute;top:0;left:0">
      <defs><linearGradient id="navyFront" x1="0" x2="1"><stop offset="0" stop-color="var(--navy)"/><stop offset=".5" stop-color="var(--navy-light)"/><stop offset="1" stop-color="var(--navy)"/></linearGradient></defs>
      <path d="M0 12 Q235 -6 470 22 L470 100 L0 100Z" fill="var(--green)"/>
      <path d="M0 22 Q235 4 470 30 L470 100 L0 100Z" fill="url(#navyFront)"/>
    </svg>
    <div class="social" aria-hidden="true"></div>
    <div class="footer__text">021 555 0148 &nbsp;| 021 555 0192<br>hello@kestrelarrivals.example<br><span class="footer__web">www.kestrelarrivals.example</span></div>
  </footer>
</section>

<section class="flyer flyer--back">
  <div class="photo photo--students" role="img" aria-label="Three smiling students studying together at a table"></div>
  <svg class="swoosh" style="top:225px" width="470" height="90" viewBox="0 0 470 90">
    <path d="M0 15 Q220 95 470 20 L470 90 L0 90Z" fill="var(--green)"/>
    <path d="M0 28 Q220 108 470 32 L470 90 L0 90Z" fill="#fff"/>
  </svg>
  <div class="badge" style="left:358px;top:232px;width:90px;height:90px" role="img" aria-label="Licensing authority badge"></div>

  <h2 class="center package-title" style="font-weight:400">KESTREL ARRIVALS PACKAGE</h2>
  <p class="body-copy" style="top:360px;left:20px">Set yourself on a clear pathway from your first student visa to permanent residency with our comprehensive immigration package.</p>
  <p class="body-copy" style="top:405px;left:20px">Connect with licensed advisers who walk alongside you in your New Zealand journey, helping to make the most of your time and money</p>

  <ul class="benefits">
    <li>Confirmed, discounted rates for ongoing visas once your study is completed</li>
    <li>A one on one session with a licensed adviser to plan how to maximise your studies &amp; work opportunities to achieve residency faster</li>
    <li>Attendance at an immigration seminar</li>
    <li>Vital updates on immigration policy changes &amp; how they impact on you</li>
    <li>Access immediate advice from someone who knows your situation if things go wrong</li>
  </ul>

  <div class="plan">
    <div class="plan__col"><span class="plan__num">1</span>Deposit of 15% which covers Post Study Open Visa (job search)</div>
    <div class="plan__col plan__col--shade"><span class="plan__num">2</span>Either Post Study Employer Assisted Visa or Essential Skills Work Visa (this includes employer support)</div>
    <div class="plan__col"><span class="plan__num">3</span>Either Skilled Migrant Category Residence or Work to Residence Visa (both components for latter)</div>
  </div>
  <div class="pill" style="left:37px;top:613px;width:398px;height:30px;line-height:30px;font-size:13px">Our Kestrel Arrivals Package includes 3 visa applications</div>

  <p class="center addons">Add on’s for family and work options available.</p>
  <p class="center tagline">Let Marlow Bay Kestrel Arrivals plan your route to residency.</p>

  <div class="logo" style="left:20px;top:832px;gap:10px">
    <div class="logo__mark" style="width:50px;height:50px;border-width:5px"></div>
    <div class="logo__name" style="font-size:14px;padding-left:6px">Marlow Bay<br>Kestrel Arrivals<br><span style="font-size:9px;letter-spacing:1.5px">Immigration Advice</span></div>
  </div>

  <dl class="contacts">
    <dt>Isla <span>&#9742; 021 555 0148</span></dt>
    <dd>License Number 209900417</dd>
    <dt>Maren <span>&#9742; 021 555 0192</span></dt>
    <dd>License Number 209900583</dd>
  </dl>

  <footer class="footer">
    <svg width="470" height="100" viewBox="0 0 470 100" style="position:absolute;top:0;left:0">
      <defs><linearGradient id="navyBack" x1="0" x2="1"><stop offset="0" stop-color="var(--navy)"/><stop offset=".5" stop-color="var(--navy-light)"/><stop offset="1" stop-color="var(--navy)"/></linearGradient></defs>
      <path d="M0 12 Q235 -6 470 22 L470 100 L0 100Z" fill="var(--green)"/>
      <path d="M0 22 Q235 4 470 30 L470 100 L0 100Z" fill="url(#navyBack)"/>
    </svg>
    <div class="social" aria-hidden="true"></div>
    <div class="footer__text">021 555 0148 &nbsp;| 021 555 0192<br>hello@kestrelarrivals.example<br><span class="footer__web">www.kestrelarrivals.example</span></div>
  </footer>
</section>

</body>
</html>
```